B2B Energy Broker Website

Our current website looks amateur, we need something far more professional looking and advanced. Current website is www.kelmora-utilitylink.com

```html
<!DOCTYPE html>
<html lang="en">
<head>
<meta charset="utf-8">
<title>Kelmora Utility Link – Transparent Energy Savings</title>
<link href="https://fonts.googleapis.com/css2?family=Mulish:wght@300;400;600;700;800&display=swap" rel="stylesheet">
<style>
:root{
  --navy:#1f244b;
  --indigo:#39417e;
  --slate:#7077a3;
  --board:#e9eaee;
  --paper:#ffffff;
  --mist:#f4f4f7;
  --ink:#4a4e6a;
  --muted:#8a8ea8;
  --line:#e3e4ea;
}
*{box-sizing:border-box;margin:0;padding:0}
html,body{width:1200px;height:3698px;overflow:hidden}
body{background:var(--board);font-family:"Mulish",sans-serif;color:var(--ink);position:relative}
.abs{position:absolute}

/* style sheet header */
.brand-sheet{position:absolute;left:0;top:0;width:1200px;height:240px}
.sheet-logo{position:absolute;left:294px;top:132px;display:flex;align-items:center;gap:12px}
.dot{width:40px;height:40px;border-radius:50%;background:var(--navy)}
.wordmark{font-weight:600;font-size:22px;color:var(--indigo);letter-spacing:3px}
.sheet-rule{position:absolute;top:106px;width:1px;height:104px;background:#cfd1da}
.sheet-fonts{position:absolute;left:563px;top:104px;color:var(--slate)}
.sheet-fonts h3,.sheet-palette h3{font-weight:400;font-size:24px;color:var(--indigo);margin-bottom:18px}
.sheet-fonts p{font-weight:300;font-size:18px;line-height:24px}
.sheet-palette{position:absolute;left:764px;top:104px}
.swatches{display:flex;gap:12px}
.swatch{text-align:center;font-size:9px;color:#555}
.swatch i{display:block;width:37px;height:37px;border-radius:50%;margin-bottom:6px}

/* page */
.page{position:absolute;left:170px;top:240px;width:860px;height:3427px;background:var(--paper);overflow:hidden}
.topbar{height:27px;background:var(--slate);display:flex;justify-content:flex-end;align-items:center;gap:22px;padding-right:115px;font-size:8px;color:#fff}
.topbar span{display:flex;align-items:center;gap:5px}
.nav{height:72px;display:flex;align-items:center;justify-content:space-between;padding:0 115px}
.nav .dot{width:32px;height:32px}
.logo{display:flex;align-items:center;gap:9px}
.logo .wordmark{font-size:16px}
.nav ul{list-style:none;display:flex;gap:32px;font-size:9px;color:var(--ink)}

.hero{position:relative;height:381px}
.hero-photo{position:absolute;inset:0;background:radial-gradient(ellipse at 50% 30%,#aab0ee 0%,#6f78d6 40%,#4650ad 75%,#2f3575 100%)}
.hero-text{position:absolute;left:0;right:0;top:128px;text-align:center;color:#fff}
.eyebrow{display:inline-block;background:rgba(255,255,255,.18);padding:4px 10px;font-size:9px;letter-spacing:2px;color:#e7e8ff}
.hero h1{font-weight:800;font-size:38px;line-height:44px;margin-top:12px;text-shadow:0 2px 6px rgba(31,36,75,.45)}
.scroll-btn{position:absolute;left:411px;top:265px;width:40px;height:40px;border-radius:50%;background:#fff;display:flex;align-items:center;justify-content:center}

.intro-band{position:relative;height:156px;background:var(--slate)}
.intro-band .dark{position:absolute;left:0;top:0;width:806px;height:156px;background:var(--navy)}
.intro-band h2{position:absolute;left:115px;top:52px;font-weight:600;font-size:17px;line-height:24px;color:#fff}
.intro-band p{position:absolute;left:290px;top:42px;width:455px;font-size:8px;line-height:17px;color:#c7c9de}

.white-a{position:relative;height:1006px}
.svc{position:absolute;top:60px;height:70px;display:flex;align-items:center}
.svc b{font-weight:800;font-size:72px;color:transparent;-webkit-text-stroke:1px #d3d5e3;letter-spacing:-2px}
.svc span{position:absolute;left:32px;top:26px;font-size:12px;color:var(--indigo);white-space:nowrap}
.divider{position:absolute;left:115px;top:192px;width:630px;height:1px;background:var(--line)}
.about-frame{position:absolute;left:105px;top:286px;width:130px;height:304px;border-left:1px solid #9da0b8;border-bottom:1px solid #9da0b8}
.about-photo{position:absolute;left:115px;top:276px;width:306px;height:304px;background:linear-gradient(135deg,#dfe2ea,#c6cbd9 55%,#eef0f5)}
.about-copy{position:absolute;left:492px;top:272px;width:253px}
.about-copy h2{font-weight:600;font-size:17px;line-height:24px;color:var(--navy);margin-bottom:22px}
.about-copy p{font-size:7.5px;line-height:17px;margin-bottom:10px}
.about-copy a{color:var(--indigo);font-weight:700;text-decoration:underline}
.btn{display:inline-block;background:var(--slate);color:#fff;font-size:7px;letter-spacing:.5px;padding:11px 16px;margin-top:10px}
.call-box{position:absolute;left:115px;top:644px;width:630px;height:156px;background:var(--mist);display:flex;align-items:center;justify-content:center;font-weight:600;font-size:17px;color:var(--indigo)}
.call-box u{margin:0 6px}
.ticks{position:absolute;left:115px;top:860px;width:630px;display:grid;grid-template-columns:repeat(3,1fr);row-gap:20px;column-gap:0}
.ticks div{display:flex;align-items:center;gap:8px;font-size:7px;color:var(--ink);white-space:nowrap}

.expertise{position:relative;height:460px;margin-left:54px;background:var(--indigo)}
.expertise h2{position:absolute;left:61px;top:60px;font-weight:600;font-size:18px;line-height:27px;color:#fff}
.expertise .lead{position:absolute;left:438px;top:64px;width:253px;font-size:7.5px;line-height:17px;color:#c7c9e6}
.card{position:absolute;top:170px;width:229px;height:227px;border:1px solid #5a62a0;padding:60px 30px 0}
.card h3{font-weight:600;font-size:10px;color:#fff;margin:16px 0 12px}
.card p{font-size:7px;line-height:15px;color:#c7c9e6}

.white-b{position:relative;height:913px}
.faq-intro{position:absolute;left:115px;top:78px;width:270px}
.faq-intro h2{font-weight:600;font-size:17px;line-height:24px;color:var(--navy);margin-bottom:26px}
.faq-intro p{font-size:7.5px;line-height:17px;margin-bottom:14px}
.faq-intro a{font-size:8px;color:var(--indigo);text-decoration:underline}
.faq{position:absolute;left:437px;top:64px;width:308px}
.faq-item{border:1px solid var(--line);margin-bottom:5px;font-size:7px;color:var(--indigo)}
.faq-item .q{display:flex;justify-content:space-between;align-items:center;height:31px;padding:0 11px}
.faq-item.open .q{background:var(--mist)}
.faq-item .a{padding:10px 11px;font-size:6.5px;line-height:13px;color:var(--muted)}
.partners{position:absolute;left:115px;top:432px;width:630px;display:flex;justify-content:space-between}
.partners i{display:block;width:84px;height:30px;border-radius:4px;background:#e6e7ec}
.video{position:absolute;left:115px;top:524px;width:630px;height:215px;background:linear-gradient(110deg,#b8bfcc 0%,#dce2ee 45%,#eef2f9 100%)}
.play{position:absolute;left:288px;top:80px;width:56px;height:56px;border-radius:50%;background:var(--navy);display:flex;align-items:center;justify-content:center}
.cols{position:absolute;left:115px;top:800px;width:630px;display:grid;grid-template-columns:1fr 1fr;column-gap:122px;font-size:7.5px;line-height:16px}

.cta{height:154px;width:806px;background:var(--slate);display:flex;align-items:center;justify-content:space-between;padding:0 61px 0 115px}
.cta h2{font-weight:600;font-size:17px;color:#fff}
.cta a{background:#fff;color:var(--indigo);font-size:7px;padding:12px 18px;letter-spacing:.5px}

.footer{position:relative;height:258px;background:var(--navy);color:#c7c9de}
.footer .logo{position:absolute;left:115px;top:56px}
.footer .wordmark{color:#fff}
.footer .dot{background:#fff}
.fcol{position:absolute;top:50px;font-size:7.5px}
.fcol h4{font-weight:400;font-size:11px;letter-spacing:1px;margin-bottom:18px;color:#c7c9de}
.fcol p{margin-bottom:10px}
.fcol .pair{display:flex;gap:28px}
.vrule{position:absolute;top:0;width:1px;height:156px;background:#34396a}
.hrule{position:absolute;left:0;top:156px;width:860px;height:1px;background:#34396a}
.fbottom{position:absolute;top:196px;font-size:6.5px;color:#9da0c0}
</style>
</head>
<body>

<section class="brand-sheet">
  <div class="sheet-logo"><span class="dot"></span><span class="wordmark">KELMORA</span></div>
  <span class="sheet-rule" style="left:504px"></span>
  <div class="sheet-fonts"><h3>Fonts:</h3><p>Muli<br>Sans Serif</p></div>
  <span class="sheet-rule" style="left:706px"></span>
  <div class="sheet-palette"><h3>Color Palette:</h3>
    <div class="swatches">
      <div class="swatch"><i style="background:var(--navy)"></i>#1f244b</div>
      <div class="swatch"><i style="background:var(--indigo)"></i>#39417e</div>
      <div class="swatch"><i style="background:var(--slate)"></i>#7077a3</div>
    </div>
  </div>
</section>

<main class="page">
  <div class="topbar">
    <span><svg width="8" height="8" viewBox="0 0 10 10"><path d="M2 1l2 2-1 1.5c.7 1.3 1.3 1.9 2.5 2.5L7 6l2 2-1.5 1.5C4 9 1 6 .5 2.5z" fill="#fff"/></svg>0333 410 7725</span>
    <span><svg width="9" height="7" viewBox="0 0 10 8"><rect x=".5" y=".5" width="9" height="7" fill="none" stroke="#fff"/><path d="M.5 .5l4.5 4 4.5-4" fill="none" stroke="#fff"/></svg>info@kelmora-utilitylink.com</span>
  </div>

  <nav class="nav">
    <div class="logo"><span class="dot"></span><span class="wordmark">KELMORA</span></div>
    <ul><li>- Home</li><li>- About</li><li>- Services</li><li>- FAQs</li><li>- Contact Us</li></ul>
  </nav>

  <header class="hero">
    <div class="hero-photo" role="img" aria-label="Photo of three light bulbs in blue light"></div>
    <div class="hero-text">
      <span class="eyebrow">Unbiased For Your Business</span>
      <h1>TRANSPARENT<br>ENERGY SAVINGS</h1>
    </div>
    <div class="scroll-btn"><svg width="12" height="14" viewBox="0 0 12 14"><path d="M6 1v11M2 8l4 4 4-4" fill="none" stroke="#39417e" stroke-width="1.4"/></svg></div>
  </header>

  <section class="intro-band">
    <div class="dark"></div>
    <h2>Kelmora Utility<br>Link</h2>
    <p>Along with providing competitive business energy procurement, we run a complete service solution for your ongoing energy requirements. We can take total management of your bills, supplier relationships, renewals and more. If you are concerned about a more complex arrangement for your energy supply then we will endeavour to take over the time spent on it and allow you as much or as little involvement as you desire.</p>
  </section>

  <section class="white-a">
    <div class="svc" style="left:115px"><b>01</b><span>Commercial Gas</span></div>
    <div class="svc" style="left:268px"><b>02</b><span>Commercial Electricity</span></div>
    <div class="svc" style="left:456px"><b>03</b><span>Utility Services</span></div>
    <div class="svc" style="left:598px"><b>04</b><span>Commercial Water</span></div>
    <div class="divider"></div>

    <div class="about-frame"></div>
    <div class="about-photo" role="img" aria-label="Photo of an electricity bill with a calculator"></div>
    <div class="about-copy">
      <h2>About Kelmora<br>Utility Link</h2>
      <p>Kelmora Utility Link has been founded on a wealth of 30 years of commercial energy expertise with a mission to provide customers with a fresh approach to business utility services.</p>
      <p>Developing a large network of <a>over 18 energy suppliers</a>, Kelmora breaks the mould, offering clear &amp; transparent cost reducing solutions in what can be a complicated and overwhelming process. The wholesale power, gas and water markets are monitored daily; this means that you, the client, will be provided with the right product offer, the best prices and first class customer service.</p>
      <span class="btn">LEARN MORE</span>
    </div>

    <div class="call-box">Call Kelmora Now On <u>0333 410 7725</u> To Start Saving</div>

    <div class="ticks">
      <div><svg width="9" height="9" viewBox="0 0 10 10"><circle cx="5" cy="5" r="4.3" fill="none" stroke="#7077a3"/><path d="M3 5l1.5 1.5L7 3.8" fill="none" stroke="#7077a3"/></svg>Lorem ipsum dolor sit amet dummy text</div>
      <div><svg width="9" height="9" viewBox="0 0 10 10"><circle cx="5" cy="5" r="4.3" fill="none" stroke="#7077a3"/><path d="M3 5l1.5 1.5L7 3.8" fill="none" stroke="#7077a3"/></svg>Lorem ipsum dolor sit amet dummy text</div>
      <div><svg width="9" height="9" viewBox="0 0 10 10"><circle cx="5" cy="5" r="4.3" fill="none" stroke="#7077a3"/><path d="M3 5l1.5 1.5L7 3.8" fill="none" stroke="#7077a3"/></svg>Lorem ipsum dolor sit amet dummy text</div>
      <div><svg width="9" height="9" viewBox="0 0 10 10"><circle cx="5" cy="5" r="4.3" fill="none" stroke="#7077a3"/><path d="M3 5l1.5 1.5L7 3.8" fill="none" stroke="#7077a3"/></svg>Lorem ipsum dolor sit amet dummy text</div>
      <div><svg width="9" height="9" viewBox="0 0 10 10"><circle cx="5" cy="5" r="4.3" fill="none" stroke="#7077a3"/><path d="M3 5l1.5 1.5L7 3.8" fill="none" stroke="#7077a3"/></svg>Lorem ipsum dolor sit amet dummy text</div>
      <div><svg width="9" height="9" viewBox="0 0 10 10"><circle cx="5" cy="5" r="4.3" fill="none" stroke="#7077a3"/><path d="M3 5l1.5 1.5L7 3.8" fill="none" stroke="#7077a3"/></svg>Lorem ipsum dolor sit amet dummy text</div>
      <div><svg width="9" height="9" viewBox="0 0 10 10"><circle cx="5" cy="5" r="4.3" fill="none" stroke="#7077a3"/><path d="M3 5l1.5 1.5L7 3.8" fill="none" stroke="#7077a3"/></svg>Lorem ipsum dolor sit amet dummy text</div>
      <div><svg width="9" height="9" viewBox="0 0 10 10"><circle cx="5" cy="5" r="4.3" fill="none" stroke="#7077a3"/><path d="M3 5l1.5 1.5L7 3.8" fill="none" stroke="#7077a3"/></svg>Lorem ipsum dolor sit amet dummy text</div>
      <div><svg width="9" height="9" viewBox="0 0 10 10"><circle cx="5" cy="5" r="4.3" fill="none" stroke="#7077a3"/><path d="M3 5l1.5 1.5L7 3.8" fill="none" stroke="#7077a3"/></svg>Lorem ipsum dolor sit amet dummy text</div>
    </div>
  </section>

  <section class="expertise">
    <h2>Our Experience Enables Us<br>To Provide In-depth Material<br>Sourcing For Every Step!</h2>
    <p class="lead">Lorem ipsum dolor sit amet, consectetur adipiscing elit, sed do eiusmod tempor incididunt ut labore et dolore magna aliqua. Quis ipsum suspendisse ultrices gravida. Risus commodo viverra maecenas accumsan lacus vel facilisis.</p>
    <div class="card" style="left:61px">
      <svg width="30" height="26" viewBox="0 0 30 26"><path d="M3 24h24M7 24v-7M13 24v-11M19 24v-8M25 24V6M5 14l7-6 6 5 9-10" fill="none" stroke="#fff" stroke-width="1.2"/></svg>
      <h3>Market Trend Analysis</h3>
      <p>Our energy analysts monitor a live energy market curve to ensure you buy at the right time and save as much as possible.</p>
    </div>
    <div class="card" style="left:321px">
      <svg width="30" height="26" viewBox="0 0 30 26"><path d="M2 10l6-4 5 2 4-2 6 3 5-2M8 7l-4 7 5 5 4-1 5 3 6-8M13 12l3 3M16 10l4 4" fill="none" stroke="#fff" stroke-width="1.2"/></svg>
      <h3>Direct Relationships</h3>
      <p>We hold direct relationships with over 18 major suppliers, we use these relationships to ensure you get the most from them.</p>
    </div>
    <div class="card" style="left:579px">
      <svg width="30" height="26" viewBox="0 0 30 26"><circle cx="20" cy="7" r="4" fill="none" stroke="#fff" stroke-width="1.2"/><path d="M3 20c4-1 6-4 10-4h5M3 24h8l9-5 6-5M12 11l-2 4" fill="none" stroke="#fff" stroke-width="1.2"/></svg>
      <h3>Industry Experiences</h3>
      <p>Our two founders hold over 30 years industry experience between them and our staff are the best in the industry.</p>
    </div>
  </section>

  <section class="white-b">
    <div class="faq-intro">
      <h2>Why Should Your Business<br>Use Kelmora Utility Link?</h2>
      <p>We provide an unbiased &amp; transparent cost effective solution to all your business energy needs, in essence, with over 3 decades experience in the UK energy industry.</p>
      <p>We have both the expertise &amp; know how to manage your business energy requirements. Our philosophy is simple solutions with transparency.</p>
      <a>Go to FAQs Page &nbsp;→</a>
    </div>
    <div class="faq">
      <div class="faq-item open"><div class="q">Why Should I Consider Using Kelmora Utility Link?<span>–</span></div>
        <div class="a">Any association, business type, charity, council, not for profit organisation or any other user of energy not paid for by non domestic entity.</div></div>
      <div class="faq-item"><div class="q">Is Kelmora Utility Link Independent?<span>+</span></div></div>
      <div class="faq-item"><div class="q">Will There Be a Charge For Gaining Quotations?<span>+</span></div></div>
      <div class="faq-item"><div class="q">How Do Kelmora Utility Link Get Paid?<span>+</span></div></div>
      <div class="faq-item"><div class="q">How Do You Achieve Better Prices Than If I Go Direct?<span>+</span></div></div>
    </div>

    <div class="partners"><i></i><i></i><i></i><i></i><i></i></div>

    <div class="video" role="img" aria-label="Photo of an electricity meter on a pale wall">
      <div class="play"><svg width="16" height="18" viewBox="0 0 16 18"><path d="M3 2l11 7-11 7z" fill="#fff"/></svg></div>
    </div>

    <div class="cols">
      <p>Lorem ipsum dolor sit amet, consectetur adipiscing elit, sed do eiusmod tempor incididunt ut labore et dolore magna aliqua. Quis ipsum suspendisse ultrices gravida. Risus commodo viverra.</p>
      <p>Sed ut perspiciatis unde omnis iste natus error sit voluptatem accusantium doloremque laudantium, totam rem aperiam, eaque ipsa quae ab illo inventore veritatis.</p>
    </div>
  </section>

  <section class="cta">
    <h2>Want To Work Together? Let's Do It!</h2>
    <a>CONTACT US</a>
  </section>

  <footer class="footer">
    <div class="logo"><span class="dot"></span><span class="wordmark">KELMORA</span></div>
    <span class="vrule" style="left:345px"></span>
    <span class="vrule" style="left:583px"></span>
    <div class="fcol" style="left:380px"><h4>QUICK LINKS</h4>
      <div class="pair"><p>Home</p><p>About</p></div>
      <div class="pair"><p>Services</p><p>Contact</p></div>
    </div>
    <div class="fcol" style="left:626px"><h4>CONTACT</h4><p>0333 410 7725</p><p>info@kelmora-utilitylink.com</p></div>
    <div class="hrule"></div>
    <div class="fbottom" style="left:115px">
      <svg width="18" height="9" viewBox="0 0 18 9"><rect x="0" y="0" width="7" height="9" fill="#c7c9de"/><rect x="10" y="0" width="7" height="9" fill="#c7c9de"/></svg>
    </div>
    <div class="fbottom" style="left:354px">© Kelmora Utility Link 2021 - All Rights Reserved</div>
    <div class="fbottom" style="left:637px">Privacy Policy &nbsp;|&nbsp; Terms &amp; Conditions</div>
  </footer>
</main>

</body>
</html>
```